Rebrand stationary with recently completed logo design

Need new business cards, thank you cards, letterhead, envelopes and presentation folders. The designs will be sent to a separate production firm so I need the files to be print ready.

My contact info
Reno Vasquell

Office 604-381-5047
Fax 604-317-4860

Email reno@glazemark.ca
website www.glazemark.ca

315-20740 47th Avenue,
Langley, BC, V2K 3P8

Target Market(s)

Homeowners, businesses and contractors

Industry/Entity Type

Business

Font styles to use
Sans Serif

Colors
34a7d7

Requirements
Must have
• Like to have one side of the business card a solid color with the logo in all white. The side with all the text to be a white background
• I find the current blue on the front of the card with the white logo too dark.
Should not have
• Gradient colors

```html
<!DOCTYPE html>
<html lang="en">
<head>
<meta charset="utf-8">
<title>Glazemark Letterhead</title>
<link rel="stylesheet" href="https://fonts.googleapis.com/css2?family=Montserrat:ital,wght@0,400;0,500;0,700;1,700&display=swap">
<style>
  :root {
    --brand-blue: #34a7d7;
    --ink: #2b2b2b;
    --rule: #9a9a9a;
    --paper: #ffffff;
  }
  html, body {
    margin: 0;
    padding: 0;
    overflow: hidden;
    background: var(--paper);
  }
  .letterhead {
    position: relative;
    width: 849px;
    height: 1200px;
    background: var(--paper);
    font-family: "Montserrat", sans-serif;
    color: var(--ink);
    overflow: hidden;
  }
  .company-name {
    position: absolute;
    left: 79px;
    top: 86px;
    margin: 0;
    font-size: 22px;
    font-weight: 500;
    line-height: 26px;
    color: var(--ink);
  }
  .contact {
    position: absolute;
    right: 80px;
    top: 38px;
    text-align: right;
    font-size: 12.5px;
    line-height: 17px;
  }
  .contact p { margin: 0; }
  .contact .value {
    font-weight: 700;
    font-style: italic;
  }
  .contact .gap { margin-top: 6px; }
  .contact .address { margin-top: 8px; }
  .header-rule {
    position: absolute;
    left: 76px;
    right: 76px;
    top: 158px;
    height: 0;
    border-top: 1px solid var(--rule);
  }
</style>
</head>
<body>
  <main class="letterhead">
    <header>
      <p class="company-name">Glazemark</p>
      <div class="contact">
        <p>Office <span class="value">604-381-5047</span></p>
        <p>Fax <span class="value">604-317-4860</span></p>
        <p class="gap">Email <span class="value">reno@glazemark.ca</span></p>
        <p>Website <span class="value">www.glazemark.ca</span></p>
        <div class="address">
          <p>315-20740 47th Avenue,</p>
          <p>Langley, BC, V2K 3P8</p>
        </div>
      </div>
      <div class="header-rule"></div>
    </header>
  </main>
</body>
</html>
```